Business Card Design Project

We require a business card template to cover basic contact information - our company logo, names of employees, title, mobile and email.

Target Market(s)

Corporate

Industry/Entity Type

Business

Font styles to use
Sans Serif

Requirements
Nice to have
• Thinking it would be great just to have the logo taking up approximately half the space (so it goes as far across the top of the card as possible) and then contact details in the lower half of the card. Keen just to use only the two colours in the logo, on a white background.
Should not have
• No fussy drawings

```html
<!DOCTYPE html>
<html lang="en">
<head>
<meta charset="utf-8">
<title>Tidewell developments – Business Card</title>
<link rel="stylesheet" href="https://fonts.googleapis.com/css2?family=Arimo:wght@400;700&display=swap">
<style>
  :root {
    --teal: #2aa5b5;
    --blue: #2f5fae;
    --ink: #222222;
    --card: #ffffff;
    --backdrop: #8a8a8a;
  }
  html, body {
    margin: 0;
    padding: 0;
    width: 1200px;
    height: 900px;
    overflow: hidden;
    background: var(--backdrop);
    font-family: "Arimo", Arial, sans-serif;
  }
  .business-card {
    position: absolute;
    left: 150px;
    top: 200px;
    width: 900px;
    height: 500px;
    background: var(--card);
    border-radius: 28px;
    overflow: hidden;
  }
  .brand {
    position: absolute;
    left: 48px;
    top: 18px;
    width: 800px;
    color: var(--teal);
    font-weight: 400;
  }
  .brand-name {
    display: block;
    font-size: 168px;
    line-height: 1;
    letter-spacing: -4px;
  }
  .brand-tagline {
    display: block;
    text-align: right;
    font-size: 44px;
    line-height: 1;
    margin-top: -8px;
  }
  .divider {
    position: absolute;
    left: 0;
    top: 250px;
    width: 100%;
    height: 7px;
    background: linear-gradient(to right, var(--blue) 0%, var(--blue) 85%, #6f94cf 100%);
  }
  .person {
    position: absolute;
    left: 78px;
    top: 360px;
  }
  .person-name {
    margin: 0;
    font-size: 31px;
    font-weight: 400;
    letter-spacing: 3px;
    color: var(--ink);
  }
  .person-title {
    margin: 2px 0 0;
    font-size: 17px;
    letter-spacing: 2.5px;
    color: var(--blue);
    text-transform: uppercase;
  }
  .contact-list {
    position: absolute;
    left: 555px;
    top: 300px;
    margin: 0;
    padding: 0;
    list-style: none;
  }
  .contact-item {
    display: flex;
    align-items: center;
    gap: 12px;
    height: 36px;
    font-size: 20px;
    letter-spacing: 3px;
    color: var(--ink);
  }
  .contact-icon {
    width: 26px;
    height: 26px;
    flex: none;
  }
</style>
</head>
<body>
  <div class="business-card">
    <div class="brand">
      <span class="brand-name">Tidewell</span>
      <span class="brand-tagline">developments</span>
    </div>

    <div class="divider"></div>

    <div class="person">
      <p class="person-name">Maren Holt</p>
      <p class="person-title">Employees Position</p>
    </div>

    <ul class="contact-list">
      <li class="contact-item">
        <svg class="contact-icon" viewBox="0 0 26 26" aria-hidden="true">
          <rect width="26" height="26" rx="4" fill="var(--teal)"/>
          <rect x="8" y="4" width="10" height="18" rx="2" fill="none" stroke="#fff" stroke-width="1.8"/>
          <rect x="10" y="7" width="6" height="7" fill="#fff"/>
          <circle cx="13" cy="18.5" r="1.3" fill="#fff"/>
        </svg>
        <span>0400 555 218</span>
      </li>
      <li class="contact-item">
        <svg class="contact-icon" viewBox="0 0 26 26" aria-hidden="true">
          <rect width="26" height="26" rx="4" fill="var(--teal)"/>
          <rect x="4.5" y="7.5" width="17" height="11" fill="none" stroke="#fff" stroke-width="1.6"/>
          <path d="M4.5 7.5 L13 14 L21.5 7.5" fill="none" stroke="#fff" stroke-width="1.6"/>
        </svg>
        <span>maren@email.com</span>
      </li>
    </ul>
  </div>
</body>
</html>
```